Holzdesign Firma sucht stilvolles Corporate Design
Zielgruppe
Ich stelle Utensilien aus Holz für die Küche her und verkaufe diese übers Internet. In erster Linie platzsparende Messerbretter aus Holz. Meine Zielgruppe ist jeder in Deutschland der eine Küche hat und dort kocht.
Aufgabenstellung
Das Design sollte eher schlicht und innovativ wirken. Der Name WALDFUGE muss mit ihm Logo sein. Im Logo sollte auch eine Verbindung zum Holz erkennbar sein, am besten mit einem Holzbalken oder einem Baumstamm. Im Logo sollen keine Weihnachtsbäume oder ganze Bäume sichtbar sein. Die Farbwahl würde ich auf Farben die zu Holz und Natur passen eingrenzen.
Mit dem Design will ich mich von den übrigen Handwerksbetrieben abheben und nicht einfach die üblichen Standarddesigns kopieren.

```html
<!DOCTYPE html>
<html lang="de">
<head>
<meta charset="utf-8">
<title>WALDFUGE Briefbogen</title>
<link href="https://fonts.googleapis.com/css2?family=Arimo:wght@400&display=swap" rel="stylesheet">
<style>
  :root {
    --canvas: #ffffff;
    --paper: #fdfdfb;
    --ink: #111111;
    --header-black: #000000;
    --footer-grey: #8d8d86;
    --shadow: rgba(0, 0, 0, 0.35);
  }
  * { margin: 0; padding: 0; box-sizing: border-box; }
  html, body {
    width: 1200px; height: 1200px; overflow: hidden;
    background: var(--canvas);
  }
  body {
    position: relative;
    font-family: "Arimo", Arial, sans-serif;
    color: var(--ink);
  }
  .sheet {
    position: absolute;
    top: 198px;
    width: 554px; height: 783px;
    background: var(--paper);
    box-shadow: 0 12px 28px var(--shadow);
    overflow: hidden;
  }
  .sheet--left { left: 18px; }
  .sheet--right { left: 615px; }

  .header-bar {
    position: absolute; top: 0;
    background: var(--header-black);
  }
  .sheet--left .header-bar { left: 80px; width: 319px; height: 68px; }
  .sheet--right .header-bar { left: 211px; width: 343px; height: 85px; }

  .brand {
    position: absolute;
    width: 106px; height: 63px;
    display: flex; flex-direction: column; align-items: center; justify-content: flex-end;
  }
  .sheet--left .brand { left: 422px; top: 7px; }
  .sheet--right .brand { left: 80px; top: 18px; }
  .brand-dot {
    width: 22px; height: 22px; border-radius: 50%;
    background: var(--ink); margin-bottom: 8px;
  }
  .brand-name {
    font-size: 14.5px; letter-spacing: 1.2px; color: var(--ink); line-height: 1;
  }

  .sender-line {
    position: absolute; left: 80px; top: 104px;
    font-size: 7.2px;
  }
  .recipient {
    position: absolute; left: 80px; top: 117px;
    font-size: 7.2px; line-height: 8.8px;
  }
  .letter-body {
    position: absolute; left: 80px; top: 245px; width: 400px;
    font-size: 8.1px; line-height: 12px;
  }
  .letter-body p { margin-bottom: 12px; }
  .letter-body p.tight { margin-bottom: 0; }
  .closing {
    position: absolute; left: 80px; top: 570px;
    font-size: 8.1px;
  }
  .signature {
    position: absolute; left: 79px; top: 609px;
    font-size: 9px; line-height: 11px;
  }

  .footer-band {
    position: absolute; left: 0; top: 713px; width: 100%; height: 70px;
    background: var(--footer-grey);
  }
  .footer-col {
    position: absolute; top: 13px;
    font-size: 6.9px; line-height: 8.5px;
  }
  .footer-col--address { left: 80px; }
  .footer-col--contact { left: 237px; }
  .footer-col--bank { left: 408px; }
</style>
</head>
<body>

<section class="sheet sheet--left" aria-label="Briefbogen Variante Logo rechts">
  <div class="header-bar"></div>
  <div class="brand"><span class="brand-dot"></span><span class="brand-name">WALDFUGE</span></div>
  <p class="sender-line">Name • Adresse 1 • Adresse 2</p>
  <p class="recipient">Max Mustermann<br>Straße<br>Ort</p>
  <div class="letter-body">
    <p>Sehr geehrter Herr,</p>
    <p>Esse ut ex. Sed esse mollit quis laboris in pariatur, anim ut aliquip ullamco voluptate. Ex consectetur culpa in eu, proident aliqua mollit sint reprehenderit?</p>
    <p>Incididunt ut in dolore reprehenderit aliqua ad, mollit anim fugiat ea. Enim consequat ad, ipsum ad sint culpa amet consectetur, sed cupidatat. Sit commodo ut. Non, nisi excepteur, fugiat voluptate ullamco eu labore: Pariatur sint laboris. Ipsum ea culpa qui nisi id exercitation, voluptate sit qui esse. Nisi, sunt ipsum occaecat commodo ut, magna veniam sed sit. Nisi officia minim reprehenderit dolore exercitation in fugiat, pariatur do reprehenderit dolore? Dolore, nostrud dolor velit.</p>
    <p class="tight">Aute aliqua, sed nostrud ut in ex nulla id ut non mollit aute voluptate. Occaecat anim ea nostrud et dolor est fugiat tempor excepteur. Amet, esse culpa commodo proident ut commodo do aute.</p>
    <p>Qui sed adipisicing voluptate est. Fugiat sint veniam in duis non deserunt sint commodo: Occaecat dolore magna ea mollit, enim dolor exercitation dolore sunt magna aute lorem ea ad exercitation?</p>
    <p>Consectetur id ea proident. Dolore sunt velit et reprehenderit aliqua eiusmod. Exercitation eu laboris ex occaecat deserunt dolore et excepteur sint in dolore nostrud laboris dolore culpa quis cupidatat. Ea cillum et. In, consectetur amet.</p>
    <p>In elit ullamco culpa, enim reprehenderit est dolore magna, ad lorem. Ipsum ea, minim mollit sit minim. Sed voluptate velit dolor in magna non aliqua cillum in officia in excepteur.Officia veniam ut, pariatur ad veniam reprehenderit ex sint consequat magna. Amet sunt, duis velit do qui culpa, adipisicing sint mollit officia in culpa aliqua. Lorem, aliqua non labore est enim. Ad officia commodo do eu consequat. Sunt in, eu cupidatat, qui aute proident, adipisicing fugiat dolore velit ut in sint eiusmod commodo laboris do.</p>
  </div>
  <p class="closing">Mit freundlichen Grüßen</p>
  <p class="signature">Name<br>Geschäftsführer</p>
  <footer class="footer-band">
    <p class="footer-col footer-col--address">Name<br>Adresse 1<br>Adresse 2</p>
    <p class="footer-col footer-col--contact">Tel.: +49 (0) 123456<br>Fax.: +49 (0) 123456<br>E-mail: info@waldfuge-post.de</p>
    <p class="footer-col footer-col--bank">Bankverbindung: xxxxxxxxxx<br>IBAN: xxxxxxxxxxxxxx<br>BIC: xxxxxxxxxxxxxxxxxx</p>
  </footer>
</section>

<section class="sheet sheet--right" aria-label="Briefbogen Variante Logo links">
  <div class="header-bar"></div>
  <div class="brand"><span class="brand-dot"></span><span class="brand-name">WALDFUGE</span></div>
  <p class="sender-line">Name • Adresse 1 • Adresse 2</p>
  <p class="recipient">Max Mustermann<br>Straße<br>Ort</p>
  <div class="letter-body">
    <p>Sehr geehrter Herr,</p>
    <p>Esse ut ex. Sed esse mollit quis laboris in pariatur, anim ut aliquip ullamco voluptate. Ex consectetur culpa in eu, proident aliqua mollit sint reprehenderit?</p>
    <p>Incididunt ut in dolore reprehenderit aliqua ad, mollit anim fugiat ea. Enim consequat ad, ipsum ad sint culpa amet consectetur, sed cupidatat. Sit commodo ut. Non, nisi excepteur, fugiat voluptate ullamco eu labore: Pariatur sint laboris. Ipsum ea culpa qui nisi id exercitation, voluptate sit qui esse. Nisi, sunt ipsum occaecat commodo ut, magna veniam sed sit. Nisi officia minim reprehenderit dolore exercitation in fugiat, pariatur do reprehenderit dolore? Dolore, nostrud dolor velit.</p>
    <p class="tight">Aute aliqua, sed nostrud ut in ex nulla id ut non mollit aute voluptate. Occaecat anim ea nostrud et dolor est fugiat tempor excepteur. Amet, esse culpa commodo proident ut commodo do aute.</p>
    <p>Qui sed adipisicing voluptate est. Fugiat sint veniam in duis non deserunt sint commodo: Occaecat dolore magna ea mollit, enim dolor exercitation dolore sunt magna aute lorem ea ad exercitation?</p>
    <p>Consectetur id ea proident. Dolore sunt velit et reprehenderit aliqua eiusmod. Exercitation eu laboris ex occaecat deserunt dolore et excepteur sint in dolore nostrud laboris dolore culpa quis cupidatat. Ea cillum et. In, consectetur amet.</p>
    <p>In elit ullamco culpa, enim reprehenderit est dolore magna, ad lorem. Ipsum ea, minim mollit sit minim. Sed voluptate velit dolor in magna non aliqua cillum in officia in excepteur.Officia veniam ut, pariatur ad veniam reprehenderit ex sint consequat magna. Amet sunt, duis velit do qui culpa, adipisicing sint mollit officia in culpa aliqua. Lorem, aliqua non labore est enim. Ad officia commodo do eu consequat. Sunt in, eu cupidatat, qui aute proident, adipisicing fugiat dolore velit ut in sint eiusmod commodo laboris do.</p>
  </div>
  <p class="closing">Mit freundlichen Grüßen</p>
  <p class="signature">Name<br>Geschäftsführer</p>
  <footer class="footer-band">
    <p class="footer-col footer-col--address">Name<br>Adresse 1<br>Adresse 2</p>
    <p class="footer-col footer-col--contact">Tel.: +49 (0) 123456<br>Fax.: +49 (0) 123456<br>E-mail: info@waldfuge-post.de</p>
    <p class="footer-col footer-col--bank">Bankverbindung: xxxxxxxxxx<br>IBAN: xxxxxxxxxxxxxx<br>BIC: xxxxxxxxxxxxxxxxxx</p>
  </footer>
</section>

</body>
</html>
```